Indie musician needs album cover art

I am an independant musician releasing my second album via digital sources. I plan to make it available on Vendly and other digital stores but primarily distribute it free through Tunegrove.

The album's music style is a blend of singer-songwriter folk, punk, alt country, electronic rock and spoken word. The lyrical content is a dark journey through travel in foreign countries, relationships, airports and theatres, formed during my own journey as an audio engineer for a travelling theatre show.

The album is called "Ash Under Glass" - at times both a plea and a directive. I would like the album cover to reflect a sense of longing, restlessness, unease and movement. A subversive tone is also possible.

I have had a go at designing a couple of ideas myself, using my own photos. I like the ideas but I am not skilled in graphic design and am unable to take them further to get the right feel and look. I will post these as examples of tone. The finished work does not need to copy either of these.

A .zip of the album can be downloaded here (low fi mp3):

http://fylo.io/Qx7rT4

Target Market(s)

People who enjoy thoughtful, honest, homemade music. Definitely not a teeny pop audience. Adult, subversive, educated, emotional...

Industry/Entity Type

Graphic Design

Requirements
Must have
• Artist name (no caps): kipwren
Album name (prefer no caps): ash under glass

```html
<!DOCTYPE html>
<html lang="en">
<head>
<meta charset="utf-8">
<title>kipwren — ash under glass</title>
<link rel="stylesheet" href="https://fonts.googleapis.com/css2?family=Arimo:wght@400;700&display=swap">
<style>
  :root {
    --page: #ffffff;
    --night-deep: #17110f;
    --night-mid: #2e2320;
    --street-warm: #6b4a3a;
    --title-band: rgba(168, 28, 22, 0.78);
    --cream: #f3e9d6;
    --rule: rgba(243, 233, 214, 0.85);
  }
  html, body {
    margin: 0;
    padding: 0;
    width: 1200px;
    height: 900px;
    overflow: hidden;
    background: var(--page);
  }
  .canvas {
    position: relative;
    width: 1200px;
    height: 900px;
    background: var(--page);
  }
  .album-cover {
    position: absolute;
    left: 258px;
    top: 108px;
    width: 683px;
    height: 683px;
    overflow: hidden;
  }
  .cover-photo {
    position: absolute;
    inset: 0;
    background:
      radial-gradient(ellipse 45% 35% at 25% 22%, rgba(217, 180, 138, 0.55), transparent 70%),
      radial-gradient(ellipse 30% 20% at 80% 42%, rgba(217, 160, 110, 0.35), transparent 70%),
      radial-gradient(ellipse 40% 25% at 30% 65%, rgba(150, 120, 110, 0.35), transparent 70%),
      linear-gradient(180deg, var(--night-mid) 0%, var(--night-deep) 35%, var(--street-warm) 62%, var(--night-mid) 85%, var(--night-deep) 100%);
  }
  .artist-band {
    position: absolute;
    left: 204px;
    top: 297px;
    width: 276px;
    height: 87px;
    background: var(--title-band);
  }
  .divider {
    position: absolute;
    inset: 0;
  }
  .artist-name {
    position: absolute;
    left: 266px;
    top: 294px;
    margin: 0;
    font-family: "Arimo", Arial, sans-serif;
    font-weight: 700;
    font-size: 41px;
    letter-spacing: -0.5px;
    line-height: 87px;
    color: var(--cream);
  }
  .album-title {
    position: absolute;
    left: 412px;
    top: 470px;
    margin: 0;
    font-family: "Arimo", Arial, sans-serif;
    font-weight: 400;
    font-size: 21px;
    line-height: 1;
    color: var(--cream);
    white-space: nowrap;
  }
</style>
</head>
<body>
  <main class="canvas">
    <section class="album-cover">
      <div class="cover-photo" role="img" aria-label="Night street festival photo: strings of warm lights overhead, a balloon seller crouched by the kerb and a crowd fading into the distance"></div>
      <div class="artist-band"></div>
      <svg class="divider" width="683" height="683" viewBox="0 0 683 683" aria-hidden="true">
        <line x1="522" y1="150" x2="375" y2="534" stroke="var(--rule)" stroke-width="1.5"/>
      </svg>
      <h1 class="artist-name">kipwren</h1>
      <h2 class="album-title">ash under glass</h2>
    </section>
  </main>
</body>
</html>
```